Tech website for innovative new Aerospace company

We need a website for our Aerospace tech business. We build Test equipment for major Aerospace companies like Talvorn. I would like to have a website that differentiates us from other companies like ours such as. The links below are whats typical in our line of work. You can see the "test systems" all over these sites. This is the type of thing we build. We have an innovative new way of building these test systems that will change how the entire industry views companies like mine. The website should be visually appealing and say to the customer they should expect more than just an information and link repository.

http://www.quenlix.com/
https://www.brivo-a-tek.de/en/
https://www.tolvane.com/en/home/

You can see there is just a bunch of stuff about the company whose site the customer has come to. Now the customer has to figure out how what they need might be organized in all of this noise about News and solutions, etc. I want a website that is very customer focused - meaning "what did they come here to do"? The closest I have seen to this is from another company like ours

https://www.crestmarkusa.com/

Its still not quite what I'm looking for. Customers want to do more than just investigate potential areas of expertise I do want a part of the main page to say very clearly what it is we do, but the rest of it need to be customer focused around the task they want to do. Examples are

Learn about our modular system integration solution
Configure a test system
Get a quote or place an order
Get support
Browse products and get technical specs
Understand and lower your total cost of test
Company information
Contact us
Careers

Certain tasks like configure a system should be more prominent than others like company information

I'd like a few different types of pages designed

The product pages (don't need ecommerce) need to be hierarchical by category and allow engineers to find the product that meets their specs quickly. It should not be sales focused with too many moving marketing graphics. For example, those same pages displays the information

http://www.quenlix.com/products
https://www.brivo-a-tek.de/en/products/
https://www.tolvane.com/en/products/

The products, basic specs, price and links to manuals and data sheets should be prominently displayed and easy to compare between products

For marketing content I'd like a page design that allow for the content to be structured like a magazine page with infographics and visually appealing places to embed pictures and videos. I'll create content with info graphics that match the theme of the site. I'll need a content management system so that pages can be updated and modified to some extent without a professional website builder managing all content pushes.

For pages like support, ordering, getting a quote. It should be super easy for them to just get to where they need - whether they are looking for the phone number, contact form, downloadable order sheets etc

I am looking for a smart design concept with some dummy content in it. Once I winnow in on something that appeals to me I'll provide some more content to those I think are on the right track

Target Market(s)

Aerospace Engineers
Other Test equipment providers
Managers and leaders at Aerospace companies who are looking for a partner

Need an upscale card

Font styles to use
Sans Serif

Colors
0555a3
f37122
474747
eaeaea

Requirements
Must have
• thicker cardstock
• two tone, different color on front and back
• bevel on one corner only
• Large size company logo with logo glossy or partially glossy. Surprise me with something visually and textually interesting
Nice to have
• I personally like the type of orange listed below, but it doesn't strictly fit into our blue/grey company colors. Would be glad to see someone make it work.
• Potentially orange on back side of cardstock, grey the other, or something like that
Should not have
• Dont look anything like a standard white business card, but don't go too crazy on layout. Still has to be crisp and professional for other high level executive recipients in the Aerospace industry

```html
<!DOCTYPE html>
<html lang="en">
<head>
<meta charset="utf-8">
<title>Aerotest — Modular Test System Solutions</title>
<link href="https://fonts.googleapis.com/css2?family=Oswald:wght@400;500&family=Montserrat:wght@400;600;700&display=swap" rel="stylesheet">
<style>
:root{
  --blue:#0555a3;
  --orange:#f37122;
  --dark:#474747;
  --light:#eaeaea;
  --ink:#2e2e2e;
  --muted:#8a8a8a;
  --footer:#2f2f2f;
  --white:#ffffff;
}
*{box-sizing:border-box;margin:0;padding:0}
html,body{width:1200px;height:3125px;overflow:hidden;background:var(--white)}
body{font-family:Montserrat,Arial,sans-serif;color:var(--ink);position:relative}
.abs{position:absolute}
.display{font-family:Oswald,"Arial Narrow",sans-serif;font-weight:500}
.btn{display:flex;align-items:center;justify-content:center;font-size:10px;font-weight:700;letter-spacing:.5px;color:var(--white);text-transform:uppercase}
.btn-dark{background:var(--dark);border-radius:3px;width:118px;height:34px}
.body-copy{font-size:11px;line-height:22px;color:#6a6a6a}

/* hero */
.hero{left:0;top:0;width:1200px;height:704px;background:linear-gradient(180deg,#3c4a58 0%,#7a6250 42%,#b7814f 58%,#5b5048 78%,#2a2a2c 100%)}
.hero-shade{left:0;top:0;width:1200px;height:704px;background:linear-gradient(90deg,rgba(0,0,0,.15),rgba(0,0,0,.35))}
.logo{left:160px;top:28px;display:flex;align-items:center;gap:8px;font-weight:700;font-size:30px;color:var(--white);letter-spacing:1px}
.logo-dot{width:14px;height:14px;border-radius:50%;background:var(--blue)}
.contact-item{display:flex;gap:12px;align-items:flex-start;font-size:11px;line-height:16px;color:var(--white)}
.contact-item svg{flex:none}
.contact-sep{width:1px;height:40px;background:rgba(255,255,255,.5)}
.nav{left:300px;top:94px;width:900px;height:37px;background:var(--blue)}
.nav a{position:absolute;top:12px;font-size:10px;font-weight:600;color:var(--white);text-decoration:none;transform:translateX(-50%)}
.nav .dot{position:absolute;width:2px;height:2px;background:var(--white);top:18px}
.side-menu{left:0;top:94px;width:300px;background:var(--white)}
.side-menu a{display:block;height:67px;line-height:67px;padding-left:20px;font-size:11px;color:var(--ink);text-decoration:none;border-bottom:1px solid #ddd}
.hero-title{left:318px;top:272px;width:760px;font-size:60px;line-height:75px;color:var(--white)}
.hero-text{left:320px;top:440px;width:620px;font-size:12.5px;line-height:22px;color:var(--white)}
.btn-outline{position:absolute;left:320px;top:522px;width:122px;height:40px;border:1px solid var(--white);border-radius:3px}
.hero-arrows{left:320px;top:590px;display:flex;gap:6px}

/* what we do */
.what-title{left:140px;top:785px;width:140px;text-align:right;font-size:34px;line-height:40px;color:var(--blue)}
.what-rule{left:302px;top:768px;width:2px;height:110px;background:#cfcfcf}
.what-text{left:330px;top:768px;width:710px;font-size:11px;line-height:22px;color:#8a8a8a}

/* modular */
.band-grey{left:0;top:950px;width:1200px;height:480px;background:#f3f3f3;overflow:hidden}
.mod-photo{left:160px;top:950px;width:380px;height:480px;background:radial-gradient(circle at 52% 50%,#8e9296 0%,#4c535a 35%,#2b3037 75%)}
.mod-col{left:640px;top:1003px;width:345px}
.mod-col h2{font-size:36px;line-height:50px;color:var(--blue)}
.title-rule{height:3px;background:var(--blue)}
.mod-col .title-rule{width:78px;margin-top:10px}
.mod-col p{margin-top:19px}
.mod-col .btn{margin-top:24px;margin-left:2px}

/* offerings */
.off-col{left:160px;top:1495px;width:380px}
.off-col h2{font-size:36px;line-height:50px;color:var(--blue)}
.off-col .title-rule{width:300px;height:2px;background:#222;margin-top:5px}
.off-sub{margin-top:10px;font-size:15px;line-height:22px;font-weight:700;color:var(--ink)}
.off-col .body-copy{margin-top:22px;width:345px}
.off-col .btn{margin-top:25px;margin-left:2px}
.off-frame{left:618px;top:1505px;width:312px;height:375px;border:6px solid #eef1f5}
.off-photo{left:573px;top:1548px;width:320px;height:372px;background:linear-gradient(160deg,#1c2530 0%,#3a4a5a 40%,#6b7278 70%,#8a8c88 100%)}

/* application */
.app-band{left:0;top:1996px;width:1200px;height:317px;background:linear-gradient(180deg,#2b2d30,#3f4144 50%,#26282b)}
.app-title{left:0;top:2048px;width:1200px;text-align:center;font-size:34px;font-weight:400;color:var(--white)}
.app-sub{left:300px;top:2105px;width:600px;text-align:center;font-size:13.5px;line-height:22px;color:var(--orange)}
.app-text{left:175px;top:2165px;width:850px;text-align:center;font-size:11.5px;line-height:23px;color:var(--white)}

/* solutions */
.sol-title{left:160px;top:2376px;font-size:36px;line-height:50px;color:var(--blue)}
.sol-card{top:2458px;width:203px;height:240px}
.sol-feature{left:160px;background:#9aa4ae}
.sol-box{position:absolute;left:10px;top:10px;width:170px;height:220px;background:#e9edf3;border-right:10px solid var(--blue);display:flex;flex-direction:column;align-items:center;justify-content:center;text-align:center}
.sol-box h3{font-size:13px;font-weight:600;line-height:18px;color:var(--ink);margin-bottom:10px}
.sol-box span{font-size:8px;font-weight:700;border-bottom:1px solid var(--ink)}
.sol-arrow{top:2567px}

/* footer */
.footer{left:0;top:2775px;width:1200px;height:350px;background:var(--footer)}
.f-logo{left:160px;top:2828px;display:flex;align-items:center;gap:8px;font-size:28px;font-weight:700;color:#9a9a9a;letter-spacing:1px}
.f-text{left:160px;top:2895px;width:300px;font-size:11px;line-height:21px;color:#6e6e6e}
.f-more{left:160px;top:3033px;font-size:9px;font-weight:700;color:var(--orange)}
.f-head{font-size:11.5px;font-weight:700;color:var(--white)}
.f-list{font-size:11px;line-height:22px;color:#8a8a8a}
.f-contact{display:flex;gap:12px;font-size:11px;line-height:16px;color:#8a8a8a}
.f-line{left:160px;top:3068px;width:880px;height:1px;background:#454545}
.f-copy{left:160px;top:3090px;font-size:10px;color:#777}
.social{top:3080px;width:26px;height:26px;background:#444}
</style>
</head>
<body>

<!-- HERO -->
<div class="abs hero" role="img" aria-label="Passenger jet parked on an airport apron at sunset, seen head-on"></div>
<div class="abs hero-shade"></div>

<div class="abs logo"><span>Aerotest</span><span class="logo-dot"></span></div>

<div class="abs contact-item" style="left:520px;top:32px">
  <svg width="14" height="18" viewBox="0 0 14 18"><path d="M7 0C3 0 0 3 0 7c0 5 7 11 7 11s7-6 7-11c0-4-3-7-7-7zm0 10a3 3 0 110-6 3 3 0 010 6z" fill="#0555a3"/></svg>
  <span>Location : Lorem ipsum is<br>text printing industry.</span>
</div>
<div class="abs contact-sep" style="left:705px;top:28px"></div>
<div class="abs contact-item" style="left:725px;top:32px">
  <svg width="16" height="16" viewBox="0 0 16 16"><path d="M3 1l3 3-2 2c1 2 3 4 5 5l2-2 3 3-2 3C6 15 1 10 0 3z" fill="#0555a3"/></svg>
  <span>+1 555 014 2791<br>+1 555 019 2694</span>
</div>
<div class="abs contact-sep" style="left:860px;top:28px"></div>
<div class="abs contact-item" style="left:882px;top:32px">
  <svg width="18" height="14" viewBox="0 0 18 14"><rect width="18" height="14" rx="1" fill="#0555a3"/><path d="M1 1l8 6 8-6" stroke="#fff" fill="none"/></svg>
  <span>E-mail :<br>solutions@aerotest.us</span>
</div>

<nav class="abs nav">
  <a style="left:235px">HOME</a><span class="dot" style="left:288px"></span>
  <a style="left:343px">PRODUCTS</a><span class="dot" style="left:405px"></span>
  <a style="left:466px">SOLUTIONS</a><span class="dot" style="left:528px"></span>
  <a style="left:585px">COMPANY</a><span class="dot" style="left:640px"></span>
  <a style="left:708px">CONTACT US</a>
</nav>

<div class="abs side-menu">
  <a>Link 1</a><a>Link 2</a><a>Link 3</a><a>Link 4</a>
</div>

<h1 class="abs hero-title display">Reinventing Test With Modular System Solutions</h1>
<p class="abs hero-text">Aerotest has partnered with Meridian Devices to develop a modular system architecture that allows for rapid design and integration of systems of any size.</p>
<div class="btn btn-outline">GET SUPPORT</div>
<div class="abs hero-arrows">
  <svg width="20" height="20" viewBox="0 0 20 20"><circle cx="10" cy="10" r="10" fill="#fff"/><path d="M12 5l-5 5 5 5" stroke="#222" stroke-width="2" fill="none"/></svg>
  <svg width="20" height="20" viewBox="0 0 20 20"><circle cx="10" cy="10" r="10" fill="#fff"/><path d="M8 5l5 5-5 5" stroke="#222" stroke-width="2" fill="none"/></svg>
</div>

<!-- WHAT WE DO -->
<h2 class="abs what-title display">What We Do</h2>
<div class="abs what-rule"></div>
<p class="abs what-text">Aerotest has partnered with Meridian Devices to develop a modular system architecture that allows for rapid design and integration of systems of any size. For any portion of a system that truly is universal between multiple product lines, the design becomes configuration and the integration becomes assembly – all with off the shelf instrumentation and cables out to the pin. For anything that truly must be custom for a program, these components are compartmentalized and isolated, so the design of those elements does not affect the common core. When a program concludes...</p>

<!-- MODULAR -->
<div class="abs band-grey">
  <svg width="1200" height="480" style="position:absolute;left:0;top:0"><path d="M700 480L900 0h110L810 480z" fill="#fff" opacity=".5"/><path d="M1050 480L1200 120v360z" fill="#fff" opacity=".5"/></svg>
</div>
<div class="abs mod-photo" role="img" aria-label="Jet engine on a stand inside a hangar"></div>
<svg class="abs" style="left:160px;top:950px" width="380" height="480"><rect x="25" y="25" width="330" height="430" fill="none" stroke="#fff" stroke-opacity=".7" stroke-width="3"/></svg>
<div class="abs mod-col">
  <h2 class="display">Modular System Solutions</h2>
  <div class="title-rule"></div>
  <p class="body-copy">Aerotest has partnered with Meridian Devices to develop a modular system architecture that allows for rapid design and integration of systems of any size. For any portion of a system that truly is universal between multiple product lines, the design becomes configuration and the integration becomes assembly – all with off the shelf instrumentation and cables out to the pin. For anything that truly must be custom for a program, these components are compartmentalized and isolated, so the design of those elements does not affect the common core. When a program concludes...</p>
  <div class="btn btn-dark">LEARN MORE</div>
</div>

<!-- OFFERINGS -->
<div class="abs off-col">
  <h2 class="display">Aerotest Offerings</h2>
  <div class="title-rule"></div>
  <p class="off-sub">Aerotest is ready to help you implement a reconfigurable test standard....</p>
  <p class="body-copy">Aerotest has partnered with Meridian Devices to develop a modular system architecture that allows for rapid design and integration of systems of any size. For any portion of a system that truly is universal between multiple product lines, the design becomes configuration and the integration becomes assembly – all with off the shelf instrumentation and cables out to the pin. For anything that truly must be custom for a program, these components are compartmentalized and isolated, so the design of those elements does not affect the common core. When a program concludes...</p>
  <div class="btn btn-dark">LEARN MORE</div>
</div>
<div class="abs off-frame"></div>
<div class="abs off-photo" role="img" aria-label="Ground crew loading an aircraft cargo hold with a red loader at night"></div>

<!-- APPLICATION -->
<div class="abs app-band" role="img" aria-label="Dimmed hangar interior with an aircraft under maintenance"></div>
<h2 class="abs app-title display">Application and Industry Expertise</h2>
<p class="abs app-sub">Proven best in class solutions Prototyping, Verification &amp; Validation, Production and Aftermarket Testing for Aerospace LRU Programs</p>
<p class="abs app-text">Aerotest has partnered with Meridian Devices to develop a modular system architecture that allows for rapid design and integration of systems of any size. For any portion of a system that truly is universal between multiple product lines, the design becomes configuration and the integration becomes assembly – all with off the shelf instrumentation and cables out to the pin. For anything that truly must be custom for a program, these components are compartmentalized and isolated, so the design of those elements does not affect the common core.</p>

<!-- SOLUTIONS -->
<h2 class="abs sol-title display">Solution</h2>
<div class="abs sol-card sol-feature" role="img" aria-label="Technician working inside an aircraft">
  <div class="sol-box"><h3>AUTOMATED TEST<br>SOLUTIONS</h3><span>LEARN MORE</span></div>
</div>
<div class="abs sol-card" style="left:385px;background:linear-gradient(160deg,#6d7176,#a8a9a6 50%,#4d5258)" role="img" aria-label="Close view of aircraft engine components and wiring"></div>
<div class="abs sol-card" style="left:612px;background:linear-gradient(170deg,#8e9090,#5d5f60 55%,#3a3b3c)" role="img" aria-label="Aircraft landing gear in a hangar"></div>
<div class="abs sol-card" style="left:836px;background:linear-gradient(160deg,#1c2530,#3a4a5a 45%,#7a7c78)" role="img" aria-label="Ground crew at an aircraft cargo door"></div>
<svg class="abs sol-arrow" style="left:132px" width="22" height="22" viewBox="0 0 22 22"><circle cx="11" cy="11" r="11" fill="#111"/><path d="M13 6l-5 5 5 5" stroke="#fff" stroke-width="2" fill="none"/></svg>
<svg class="abs sol-arrow" style="left:1046px" width="22" height="22" viewBox="0 0 22 22"><circle cx="11" cy="11" r="11" fill="#111"/><path d="M9 6l5 5-5 5" stroke="#fff" stroke-width="2" fill="none"/></svg>

<!-- FOOTER -->
<footer class="abs footer"></footer>
<div class="abs f-logo"><span>Aerotest</span><span class="logo-dot"></span></div>
<p class="abs f-text">Aerotest has partnered with Meridian Devices to develop a modular system architecture that allows for rapid design and integration of systems of any size. For any portion of a system that truly is universal between multiple product lines, the design becomes configuration and the integration...</p>
<div class="abs f-more">→&nbsp; LEARN MORE</div>

<div class="abs f-head" style="left:520px;top:2852px">CONTACT US</div>
<div class="abs f-contact" style="left:520px;top:2890px">
  <svg width="18" height="18" viewBox="0 0 18 18"><circle cx="9" cy="9" r="8.5" fill="none" stroke="#777"/><path d="M6 5l2 2-1 1c1 1 2 2 3 2l1-1 2 2-1 1c-3 0-6-3-6-6z" fill="#777"/></svg>
  <span>Call Us :<br>+1 555 013 4891</span>
</div>
<div class="abs f-contact" style="left:520px;top:2942px">
  <svg width="18" height="18" viewBox="0 0 18 18"><circle cx="9" cy="9" r="8.5" fill="none" stroke="#777"/><rect x="5" y="6" width="8" height="6" fill="none" stroke="#777"/><path d="M5 6l4 3 4-3" stroke="#777" fill="none"/></svg>
  <span>E-mail Us :<br>info@aerotest.com</span>
</div>
<div class="abs f-contact" style="left:520px;top:2994px">
  <svg width="18" height="18" viewBox="0 0 18 18"><circle cx="9" cy="9" r="8.5" fill="none" stroke="#777"/><path d="M9 4a3 3 0 00-3 3c0 3 3 6 3 6s3-3 3-6a3 3 0 00-3-3z" fill="#777"/></svg>
  <span>Location :<br>Lorem Ipsum is sumy text industry<br>printing when an text...</span>
</div>

<div class="abs f-head" style="left:785px;top:2852px">QUICK LINKS</div>
<div class="abs f-list" style="left:785px;top:2890px">Home<br>Products<br>Solutions<br>Company<br>Contact Us<br>Search</div>
<div class="abs f-list" style="left:920px;top:2890px">Help<br>Account<br>Terms and Condition<br>Privacy Policy</div>

<div class="abs f-line"></div>
<div class="abs f-copy">© Copyright 2018 Aerotest. All Rights Reserved.</div>
<div class="abs social" style="left:880px"></div>
<div class="abs social" style="left:912px"></div>
<div class="abs social" style="left:944px"></div>
<div class="abs social" style="left:976px"></div>

</body>
</html>
```